Tall Reed Software PowerPoint template

We are a software company selling endpoint visibility, access and security technology to enterprise-level IT departments.
Our technology helps organizations gain comprehensive visibility into and control over devices accessing their corporate network so they can quickly identify and address suspicious activity on the network that could lead to potential threats like data breaches.
This technology can cost organizations upwards of $1M - depending on the size of the organization. Our primary clients are Meridian 2,000 companies.
We want a professional, polished PowerPoint template that we can use for all company presentations. Please include:
Title page
Section page
General info page
Thank you page
Logo options and color specs are attached.
Please include our tagline on at least the title page: Discover the edge. Optimize the whole.

```html
<!DOCTYPE html>
<html lang="en">
<head>
<meta charset="utf-8">
<title>Tall Reed Software – Title Slide</title>
<link href="https://fonts.googleapis.com/css2?family=PT+Sans+Narrow:wght@400;700&family=Arimo:wght@400&display=swap" rel="stylesheet">
<style>
  :root {
    --brand-red: #8b1a1f;
    --brand-grey: #8e8e8e;
    --brand-copper: #c97f5b;
    --text-muted: #6a6a6a;
    --text-soft: #9a9a9a;
    --tint-peach: #f0d6cb;
    --tint-grey: #f2f2f2;
    --page: #ffffff;
  }
  html, body {
    margin: 0;
    padding: 0;
    overflow: hidden;
    background: var(--page);
  }
  .slide {
    position: relative;
    width: 1200px;
    height: 675px;
    overflow: hidden;
    background: var(--page);
    font-family: "PT Sans Narrow", "Arial Narrow", sans-serif;
  }
  .decor-field {
    position: absolute;
    left: 0;
    top: 30px;
    width: 432px;
    height: 645px;
    background: radial-gradient(ellipse at 38% 50%, var(--tint-peach) 0%, rgba(240,214,203,0.45) 38%, var(--tint-grey) 62%, rgba(255,255,255,0) 80%);
  }
  .tagline {
    position: absolute;
    right: 122px;
    top: 140px;
    margin: 0;
    text-align: right;
    font-weight: 700;
    font-size: 62px;
    line-height: 68px;
    letter-spacing: -0.5px;
  }
  .tagline .strong { color: var(--brand-red); }
  .tagline .link { color: var(--brand-grey); }
  .tagline .accent { color: var(--brand-copper); }
  .brand {
    position: absolute;
    right: 122px;
    top: 334px;
    display: flex;
    align-items: center;
    gap: 12px;
  }
  .brand-dot {
    width: 22px;
    height: 22px;
    border-radius: 50%;
    background: var(--brand-copper);
  }
  .brand-name {
    color: var(--brand-red);
    font-weight: 700;
    font-size: 28px;
    letter-spacing: 3px;
    text-transform: uppercase;
  }
  .divider {
    position: absolute;
    left: 740px;
    top: 391px;
    width: 338px;
    height: 1px;
    background: var(--brand-red);
  }
  .presenter {
    position: absolute;
    right: 134px;
    top: 405px;
    margin: 0;
    text-align: right;
    font-family: "Arimo", Arial, sans-serif;
    font-size: 14px;
    line-height: 18px;
    color: var(--text-muted);
  }
  .footnote {
    position: absolute;
    left: 325px;
    top: 598px;
    margin: 0;
    font-weight: 700;
    font-size: 16px;
    color: var(--text-soft);
  }
</style>
</head>
<body>
  <main class="slide">
    <div class="decor-field" role="img" aria-label="Soft field of peach and grey dots forming a diagonal brand pattern"></div>

    <h1 class="tagline">
      <span class="strong">Discover</span> <span class="link">the</span> <span class="accent">Edge</span><span class="strong">.</span><br>
      <span class="strong">Optimize</span> <span class="link">the</span> <span class="accent">Whole</span>
    </h1>

    <div class="brand">
      <span class="brand-dot"></span>
      <span class="brand-name">Tall Reed Software</span>
    </div>

    <div class="divider"></div>

    <p class="presenter">Speaker by Mr. Alan Brook<br>March 21, 2015</p>

    <p class="footnote">Lorem ipsum dolor sit amet, consectetuer adipiscing elit. Maecenas porttitor congue massa. Fusce posuere,</p>
  </main>
</body>
</html>
```